Revamp OakLionParts.com

https://oaklionparts.com/ needs a revamp. We like the general style and colors of the site, we just want to modernize the landing page, product page, view cart page, and the final confirm page.

I'm just looking for the PSD (Photoshop files) as the deliverable.

Quick Summary
Please redesign the following Pages:
1) https://oaklionparts.com/
2) https://oaklionparts.com/rubberTracks/OakLionParts/400x725nx70.php (product Page)
3) https://oaklionparts.com/viewCart.php (view cart - Add something to cart to see)
4) https://oaklionparts.com/confirmShoppingCart.php (confirm cart - Add something to cart to see)

```html
<!DOCTYPE html>
<html lang="en">
<head>
<meta charset="utf-8">
<title>OakLion Parts – Replacement Rubber Tracks</title>
<link href="https://fonts.googleapis.com/css2?family=PT+Serif:wght@400;700&family=Rubik:wght@300;400;500;700&display=swap" rel="stylesheet">
<style>
:root{
  --red:#c92d2b;
  --red-dark:#b52624;
  --gold:#d8b556;
  --sand:#ecdca9;
  --ink:#222;
  --muted:#8a8a8a;
  --card:#efe6e5;
  --line:#d9d9d9;
  --white:#fff;
  --serif:'PT Serif', Georgia, serif;
  --sans:'Rubik', Arial, sans-serif;
}
*{box-sizing:border-box;margin:0;padding:0}
html,body{width:1200px;height:3000px;overflow:hidden;background:var(--white)}
body{font-family:var(--sans);color:var(--ink);position:relative}
.abs{position:absolute}

.top-bar{left:0;top:0;width:1200px;height:6px;background:var(--red)}
.brand{left:117px;top:44px;font-family:var(--sans);font-weight:700;font-size:30px;color:var(--ink);letter-spacing:-.5px}
.shipping{left:0;width:1270px;top:64px;text-align:center;font-size:13px;font-weight:500;color:var(--red)}
.header-icons{left:950px;top:50px;display:flex;gap:20px}
.header-icons svg{width:34px;height:34px;stroke:var(--ink);fill:none;stroke-width:1.8}

.hero-art{left:0;top:0}
.hero-rule{left:0;top:606px;width:1200px;height:1px;background:var(--line)}
.hero-title{left:117px;top:250px;font-family:var(--serif);font-weight:700;font-size:31px;color:var(--red)}
.hero-sub{left:117px;top:297px;font-family:var(--serif);font-size:24px;color:var(--ink)}
.search{left:117px;top:337px;width:416px;height:58px;border:1px solid #e6e6e6;border-radius:6px;box-shadow:0 2px 6px rgba(0,0,0,.08);background:var(--white)}
.search span{position:absolute;left:24px;top:21px;font-size:12px;color:var(--muted)}
.search svg{position:absolute;right:16px;top:19px;width:20px;height:20px;stroke:var(--red);fill:none;stroke-width:2}
.popular{left:117px;top:412px;display:flex;align-items:center;gap:9px;font-size:11.5px;color:var(--muted)}
.popular .label{margin-right:12px}
.chip{border:1px solid #cfcfcf;padding:2px 9px;}
.chip.active{background:#a7a7a7;border-color:#a7a7a7;color:var(--white)}

.top-band{left:0;top:774px;width:1200px;height:667px;background:var(--gold)}
.band-kicker{left:117px;top:934px;font-family:var(--serif);font-size:21px;color:var(--ink)}
.band-title{left:117px;top:970px;font-family:var(--serif);font-weight:700;font-size:31px;color:var(--red)}
.band-quote{left:117px;top:1032px;width:420px;font-size:17px;line-height:25px;color:#2b2b2b}
.band-author{left:114px;top:1189px;font-size:17px;color:#2b2b2b}
.band-author b{font-weight:500}
.btn-shop{left:117px;top:1247px;width:166px;height:58px;background:var(--red);border-radius:4px;box-shadow:0 3px 8px rgba(0,0,0,.2);color:var(--white);font-weight:600;font-size:17px;display:flex;align-items:center;justify-content:center;gap:14px}
.btn-shop svg{width:17px;height:17px;fill:var(--white)}
.dumper-img{left:755px;top:975px;width:325px;height:210px;border-radius:30px;background:radial-gradient(ellipse at 55% 50%,#f2e21c 0%,#c9b42a 45%,rgba(90,90,90,.55) 80%,rgba(216,181,86,0) 100%)}
.stars{left:789px;top:1258px;display:flex;gap:26px}
.stars svg{width:44px;height:44px;fill:var(--white)}

.section-title{left:0;width:1200px;text-align:center;font-family:var(--serif);font-weight:700;font-size:30px;color:var(--red)}
.tabs{left:117px;top:1635px;width:966px;height:66px;display:flex;border-radius:14px;box-shadow:0 2px 10px rgba(0,0,0,.07);overflow:hidden}
.tab{flex:1;display:flex;align-items:center;justify-content:center;font-size:20px;color:var(--ink);background:var(--white);border-left:1px solid #f0f0f0;position:relative}
.tab.active{background:var(--gold);color:#f3ead0;border-left:none}
.tab.active::after{content:"";position:absolute;bottom:0;left:106px;width:108px;height:3px;background:#f3ead0}

.carousel{left:117px;top:1750px;width:966px;height:330px;overflow:hidden}
.card{position:absolute;top:0;height:322px;background:var(--card);border-radius:16px;box-shadow:0 4px 10px rgba(0,0,0,.12);overflow:hidden}
.card-photo{height:175px;background:linear-gradient(180deg,#8e9aa1 0%,#6f7a72 45%,#c99a2b 60%,#5d5a52 100%)}
.card-name{position:absolute;left:17px;top:200px;font-weight:500;font-size:15px;color:var(--ink)}
.card-size{position:absolute;left:17px;top:218px;font-size:11px;color:var(--muted)}
.card-price{position:absolute;right:17px;top:203px;font-size:12px;color:var(--red);font-weight:500}
.card-stars{position:absolute;right:17px;top:223px;display:flex;gap:7px}
.card-stars svg{width:11px;height:11px;fill:var(--gold)}
.card-btn{position:absolute;left:50%;transform:translateX(-50%);top:253px;width:166px;height:32px;border-radius:8px;background:var(--red);color:var(--white);font-size:12px;font-weight:500;display:flex;align-items:center;justify-content:center}
.arrow{width:28px;height:28px;top:1896px}
.arrow svg{width:28px;height:28px;stroke:var(--red);fill:none;stroke-width:1.6}

.field{border:1.5px solid #444;border-radius:20px;background:var(--white)}
.field .ph{position:absolute;left:68px;top:26px;font-size:16px;color:var(--muted);font-weight:300}
.field svg{position:absolute;left:42px;top:29px;width:15px;height:15px;stroke:var(--muted);fill:none;stroke-width:1.5}
.message .ph{left:60px}
.message .send{left:auto;right:22px;top:auto;bottom:20px;width:20px;height:20px;stroke:var(--red)}

.footer{left:0;top:2615px;width:1200px;height:385px;background:var(--red);color:var(--white)}
.f-mark{left:195px;top:2658px;width:42px;height:42px;border-radius:50%;background:rgba(255,255,255,.25)}
.f-brand{left:117px;top:2725px;font-size:30px;font-weight:700;color:var(--ink)}
.lock{left:117px;top:2795px;width:44px;height:52px}
.lock svg{width:44px;height:52px}
.pay-badge{left:171px;top:2808px;width:144px;height:38px;background:#1d1d1d;border-radius:5px}
.cards-row{left:117px;top:2866px;display:flex;gap:6px}
.cards-row span{width:45px;height:26px;border-radius:3px;background:var(--white)}
.cards-row span:nth-child(1){background:#2a2a2a}
.cards-row span:nth-child(4){background:#3a7bd5}
.f-head{font-size:21px;font-weight:500;color:var(--ink);top:2676px}
.disclaimer{left:366px;top:2722px;width:418px;font-size:7.6px;line-height:12.4px;font-weight:500;color:var(--ink)}
.disclaimer p+p{margin-top:10px}
.socials{left:836px;top:2720px;display:flex;gap:31px}
.socials span{width:21px;height:21px;border-radius:50%;background:var(--ink)}
.f-mail{left:836px;top:2770px;display:flex;align-items:center;gap:10px;font-size:8.5px;color:var(--ink);font-weight:500}
.f-mail svg{width:21px;height:21px}
.f-rule{left:117px;top:2948px;width:966px;height:1px;background:rgba(0,0,0,.25)}
.copyright{left:0;width:1200px;top:2965px;text-align:center;font-size:11.5px;color:var(--ink)}
</style>
</head>
<body>

<div class="abs top-bar"></div>

<header>
  <div class="abs brand">OakLion Parts</div>
  <div class="abs shipping">FREE SHIPPING IN THE U.S.A.</div>
  <nav class="abs header-icons" aria-label="Shortcuts">
    <svg viewBox="0 0 24 24" aria-label="Call"><path d="M5 3h3l2 5-2.2 1.4a11 11 0 0 0 6.8 6.8L16 14l5 2v3a2 2 0 0 1-2 2A17 17 0 0 1 3 5a2 2 0 0 1 2-2z"/><path d="M14 3a7 7 0 0 1 7 7M14 7a3 3 0 0 1 3 3"/></svg>
    <svg viewBox="0 0 24 24" aria-label="Cart"><rect x="4" y="6" width="16" height="15" rx="2"/><path d="M8 6V5a4 4 0 0 1 8 0v1M8 11a4 4 0 0 0 8 0"/></svg>
    <svg viewBox="0 0 24 24" aria-label="Menu"><path d="M3 5h18M3 12h18M3 19h18"/></svg>
  </nav>
</header>

<section class="hero">
  <svg class="abs hero-art" width="1200" height="607" viewBox="0 0 1200 607">
    <polygon points="300,607 1200,120 1200,607" fill="var(--sand)"/>
    <g role="img" aria-label="Rubber excavator tracks">
      <rect x="760" y="285" width="340" height="270" rx="90" fill="#3b3836" transform="rotate(-30 930 420)"/>
      <rect x="1095" y="385" width="160" height="185" rx="70" fill="#3b3836"/>
      <rect x="950" y="570" width="145" height="60" rx="25" fill="#3b3836"/>
    </g>
  </svg>
  <div class="abs hero-rule"></div>
  <h1 class="abs hero-title">HIGH QUALITY</h1>
  <h2 class="abs hero-sub">REPLACEMENT RUBBER TRACKS</h2>
  <div class="abs search">
    <span>Find your track SIZE</span>
    <svg viewBox="0 0 24 24"><circle cx="11" cy="11" r="7"/><path d="M16 16l5 5"/></svg>
  </div>
  <div class="abs popular">
    <span class="label">Popular :</span>
    <span class="chip">Tractor</span>
    <span class="chip">Dumper</span>
    <span class="chip active">Mini Excavator</span>
    <span class="chip">Crawler</span>
  </div>
</section>

<section class="abs top-band"></section>
<div class="abs band-kicker">TOP</div>
<h2 class="abs band-title">DUMPER RUBBER TRACKS</h2>
<p class="abs band-quote">“Lorem ipsum dolor sit amet, consectetur adipiscing elit. Porttitor yjfaucibus libero, at molestie. At turpis mi purus odio purus. Morbi montes, viverra scelerisque porttitor tortor. Turpis dui, mi ipsum velit est. Eget amet rhoncus dictum blandit amet facilisi ligula vestibulum.”</p>
<p class="abs band-author"><b>John DOE</b>, Buyer</p>
<div class="abs btn-shop">Shop Now
  <svg viewBox="0 0 24 24"><path d="M12 3l-2 2 5.5 5.5H3v3h12.5L10 19l2 2 9-9z"/></svg>
</div>
<div class="abs dumper-img" role="img" aria-label="Yellow tracked dumper machine"></div>
<div class="abs stars" aria-label="Rated 4 out of 4">
  <svg viewBox="0 0 24 24"><path d="M12 2l3 6.5 7 .8-5.2 4.8 1.4 7L12 17.6 5.8 21l1.4-7L2 9.3l7-.8z"/></svg>
  <svg viewBox="0 0 24 24"><path d="M12 2l3 6.5 7 .8-5.2 4.8 1.4 7L12 17.6 5.8 21l1.4-7L2 9.3l7-.8z"/></svg>
  <svg viewBox="0 0 24 24"><path d="M12 2l3 6.5 7 .8-5.2 4.8 1.4 7L12 17.6 5.8 21l1.4-7L2 9.3l7-.8z"/></svg>
  <svg viewBox="0 0 24 24"><path d="M12 2l3 6.5 7 .8-5.2 4.8 1.4 7L12 17.6 5.8 21l1.4-7L2 9.3l7-.8z"/></svg>
</div>

<h2 class="abs section-title" style="top:1545px">BROWSE PRODUCTS</h2>
<div class="abs tabs">
  <div class="tab active">FEATURED</div>
  <div class="tab">UTILITY TRACKS</div>
  <div class="tab">TRACKS BY BRAND</div>
</div>

<div class="abs arrow" style="left:44px"><svg viewBox="0 0 28 28"><circle cx="14" cy="14" r="12.5"/><path d="M20 14H8M13 9l-5 5 5 5"/></svg></div>
<div class="abs arrow" style="left:1128px"><svg viewBox="0 0 28 28"><circle cx="14" cy="14" r="12.5"/><path d="M8 14h12M15 9l5 5-5 5"/></svg></div>

<div class="abs carousel">
  <article class="card" style="left:-2px;width:305px">
    <div class="card-photo" role="img" aria-label="Excavator on rubber tracks"></div>
    <div class="card-name">Rubber Track</div><div class="card-size">180x72x39</div>
    <div class="card-price">$ 50</div>
    <div class="card-stars"><svg viewBox="0 0 24 24"><path d="M12 2l3 6.5 7 .8-5.2 4.8 1.4 7L12 17.6 5.8 21l1.4-7L2 9.3l7-.8z"/></svg><svg viewBox="0 0 24 24"><path d="M12 2l3 6.5 7 .8-5.2 4.8 1.4 7L12 17.6 5.8 21l1.4-7L2 9.3l7-.8z"/></svg><svg viewBox="0 0 24 24"><path d="M12 2l3 6.5 7 .8-5.2 4.8 1.4 7L12 17.6 5.8 21l1.4-7L2 9.3l7-.8z"/></svg><svg viewBox="0 0 24 24"><path d="M12 2l3 6.5 7 .8-5.2 4.8 1.4 7L12 17.6 5.8 21l1.4-7L2 9.3l7-.8z"/></svg></div>
    <div class="card-btn">Shop Now</div>
  </article>
  <article class="card" style="left:342px;width:322px">
    <div class="card-photo" role="img" aria-label="Excavator on rubber tracks"></div>
    <div class="card-name">Rubber Track</div><div class="card-size">180x72x39</div>
    <div class="card-price">$ 50</div>
    <div class="card-stars"><svg viewBox="0 0 24 24"><path d="M12 2l3 6.5 7 .8-5.2 4.8 1.4 7L12 17.6 5.8 21l1.4-7L2 9.3l7-.8z"/></svg><svg viewBox="0 0 24 24"><path d="M12 2l3 6.5 7 .8-5.2 4.8 1.4 7L12 17.6 5.8 21l1.4-7L2 9.3l7-.8z"/></svg><svg viewBox="0 0 24 24"><path d="M12 2l3 6.5 7 .8-5.2 4.8 1.4 7L12 17.6 5.8 21l1.4-7L2 9.3l7-.8z"/></svg><svg viewBox="0 0 24 24"><path d="M12 2l3 6.5 7 .8-5.2 4.8 1.4 7L12 17.6 5.8 21l1.4-7L2 9.3l7-.8z"/></svg></div>
    <div class="card-btn">Shop Now</div>
  </article>
  <article class="card" style="left:684px;width:322px">
    <div class="card-photo" role="img" aria-label="Excavator on rubber tracks"></div>
    <div class="card-name">Rubber Track</div><div class="card-size">180x72x39</div>
    <div class="card-price">$ 50</div>
    <div class="card-stars"><svg viewBox="0 0 24 24"><path d="M12 2l3 6.5 7 .8-5.2 4.8 1.4 7L12 17.6 5.8 21l1.4-7L2 9.3l7-.8z"/></svg><svg viewBox="0 0 24 24"><path d="M12 2l3 6.5 7 .8-5.2 4.8 1.4 7L12 17.6 5.8 21l1.4-7L2 9.3l7-.8z"/></svg><svg viewBox="0 0 24 24"><path d="M12 2l3 6.5 7 .8-5.2 4.8 1.4 7L12 17.6 5.8 21l1.4-7L2 9.3l7-.8z"/></svg><svg viewBox="0 0 24 24"><path d="M12 2l3 6.5 7 .8-5.2 4.8 1.4 7L12 17.6 5.8 21l1.4-7L2 9.3l7-.8z"/></svg></div>
    <div class="card-btn">Shop Now</div>
  </article>
</div>

<h2 class="abs section-title" style="top:2260px">GET IN TOUCH</h2>
<div class="abs field" style="left:117px;top:2317px;width:321px;height:74px">
  <svg viewBox="0 0 16 16"><circle cx="8" cy="5" r="3"/><path d="M2 15c0-3.5 3-5 6-5s6 1.5 6 5"/></svg>
  <span class="ph">Name</span>
</div>
<div class="abs field" style="left:117px;top:2419px;width:321px;height:74px">
  <svg viewBox="0 0 16 16"><rect x="1.5" y="3" width="13" height="10" rx="1"/><path d="M1.5 4l6.5 5 6.5-5"/></svg>
  <span class="ph">Email</span>
</div>
<div class="abs field message" style="left:469px;top:2317px;width:612px;height:176px">
  <span class="ph">Your Message</span>
  <svg class="send" viewBox="0 0 20 20"><path d="M2 3l16 7-16 7 3-7zM5 10h13"/></svg>
</div>

<footer class="abs footer"></footer>
<div class="abs f-mark"></div>
<div class="abs f-brand">OakLion Parts</div>
<div class="abs lock" aria-label="Secure checkout">
  <svg viewBox="0 0 44 52"><path d="M11 22v-8a11 11 0 0 1 22 0v8" fill="none" stroke="#1d1d1d" stroke-width="5"/><rect x="2" y="22" width="40" height="30" rx="4" fill="#1d1d1d"/><circle cx="22" cy="34" r="4" fill="var(--red)"/><rect x="20.5" y="35" width="3" height="9" fill="var(--red)"/></svg>
</div>
<div class="abs pay-badge"></div>
<div class="abs cards-row"><span></span><span></span><span></span><span></span></div>

<h3 class="abs f-head" style="left:366px">General Disclaimer</h3>
<div class="abs disclaimer">
  <p>All brand and model names used on this site are trademarks or registered trademarks of their respective owners, who are listed in the legal disclaimer section of our terms of use. These names are shown only to help buyers match a replacement track to their machine. Nothing on this site grants any license or right to use any mark without the written consent of its owner. All trademarks and copyrighted material remain the property of their owners, and any use of such material by OakLion Parts, LLC is for information purposes only.</p>
  <p>Product images shown here are for illustration purposes only and may not be an exact view of the product. OakLion Parts reserves the right to change product images and specifications at any time without notice.</p>
</div>

<h3 class="abs f-head" style="left:836px">Get In Touch</h3>
<div class="abs socials"><span></span><span></span><span></span></div>
<div class="abs f-mail">
  <svg viewBox="0 0 21 21"><circle cx="10.5" cy="10.5" r="10.5" fill="#222"/><rect x="5" y="6.5" width="11" height="8" rx="1" fill="none" stroke="#fff" stroke-width="1.3"/><path d="M5 7.5l5.5 4 5.5-4" fill="none" stroke="#fff" stroke-width="1.3"/></svg>
  support@oaklionparts.com
</div>
<div class="abs f-rule"></div>
<div class="abs copyright">© 2020 OakLion Parts, LLC. All Rights are Reserved. Privacy Policy | Site Map | Terms of Service</div>

</body>
</html>
```